Real Estate "For Sale" Sign for construction company

We need a sign that we can use to hang on a post and place on the road when we sell a property. The sign will be simple and will need to mainly feature our logo (files attached), as well as the words "For Sale", and then our phone number "(555) 617 3489". The sign will hang on a post that'll look something like the attached picture.

Target Market(s)

Home buyers

Industry/Entity Type

Real Estate

Font styles to use
Serif
Sans Serif

Colors
0054AA
0677BA
7BADD7
CADEEF
E8F1F8
0094D4
00A9DD
6FCCEA
C7EBF8
E9F6FB

Requirements
Must have
• For Sale & our phone number

```html
<!DOCTYPE html>
<html lang="en">
<head>
<meta charset="UTF-8">
<title>For Sale Sign – Northwood Ridge Realty</title>
<link rel="stylesheet" href="https://fonts.googleapis.com/css2?family=Poppins:wght@500;800&display=swap">
<style>
  :root {
    --sign-white: #ffffff;
    --sign-navy: #131f4b;
    --pill-blue: #213579;
    --brand-blue: #0677BA;
    --accent-line: #1e3a9e;
    --icon-cyan: #3ecbf5;
    --rule-light: #c9cce0;
  }
  html, body {
    margin: 0;
    padding: 0;
    width: 826px;
    height: 1200px;
    overflow: hidden;
    background: var(--sign-white);
  }
  .sign {
    position: relative;
    width: 826px;
    height: 1200px;
    font-family: "Poppins", Arial, sans-serif;
  }
  .brand-panel {
    position: absolute;
    inset: 0 0 auto 0;
    height: 365px;
    background: var(--sign-white);
  }
  .brand-panel__rule {
    position: absolute;
    left: 27px;
    top: 0;
    width: 2px;
    height: 344px;
    background: var(--accent-line);
  }
  .brand-mark {
    position: absolute;
    left: 358px;
    top: 88px;
    width: 110px;
    height: 110px;
    border-radius: 50%;
    background: var(--brand-blue);
  }
  .brand-name {
    position: absolute;
    left: 0;
    right: 0;
    top: 212px;
    margin: 0;
    text-align: center;
    font-weight: 500;
    font-size: 44px;
    letter-spacing: -0.5px;
    color: var(--brand-blue);
  }
  .sale-panel {
    position: absolute;
    left: 0;
    right: 0;
    top: 365px;
    bottom: 0;
    background: var(--sign-navy);
  }
  .sale-panel__rules {
    position: absolute;
    top: 15px;
    bottom: 0;
    left: 768px;
    width: 30px;
    border-left: 1px solid var(--rule-light);
    border-right: 1px solid var(--rule-light);
  }
  .sale-panel__rules::after {
    content: "";
    position: absolute;
    top: 0;
    bottom: 0;
    left: 13px;
    width: 1px;
    background: var(--rule-light);
  }
  .headline {
    position: absolute;
    left: 0;
    margin: 0;
    font-weight: 800;
    color: var(--sign-white);
    line-height: 1;
    white-space: nowrap;
  }
  .headline--for {
    left: 110px;
    top: 70px;
    font-size: 300px;
    letter-spacing: -8px;
  }
  .headline--sale {
    left: 108px;
    top: 318px;
    font-size: 256px;
    letter-spacing: -6px;
  }
  .phone-pill {
    position: absolute;
    left: 98px;
    top: 601px;
    width: 631px;
    height: 115px;
    border-radius: 58px;
    background: var(--pill-blue);
    box-shadow: 0 30px 40px -18px rgba(0, 0, 0, 0.6);
  }
  .phone-pill__icon {
    position: absolute;
    left: 24px;
    top: 18px;
    width: 78px;
    height: 78px;
  }
  .phone-pill__number {
    position: absolute;
    left: 116px;
    top: 50%;
    transform: translateY(-52%);
    margin: 0;
    font-weight: 800;
    font-size: 60px;
    letter-spacing: -1px;
    color: var(--sign-white);
    white-space: nowrap;
  }
</style>
</head>
<body>
  <main class="sign">
    <header class="brand-panel">
      <span class="brand-panel__rule"></span>
      <span class="brand-mark" aria-hidden="true"></span>
      <p class="brand-name">Northwood Ridge Realty</p>
    </header>

    <section class="sale-panel">
      <span class="sale-panel__rules"></span>
      <h1 class="headline headline--for">FOR</h1>
      <h1 class="headline headline--sale">SALE</h1>

      <div class="phone-pill">
        <svg class="phone-pill__icon" viewBox="0 0 78 78" aria-hidden="true">
          <circle cx="39" cy="39" r="39" fill="var(--icon-cyan)"/>
          <path d="M27 20c2-1 4 0 5 2l4 7c1 2 0 4-1 5l-3 2c2 5 6 9 11 11l2-3c1-1 3-2 5-1l7 4c2 1 3 3 2 5l-2 4c-1 2-3 3-6 3-15-1-28-14-29-29 0-3 1-5 3-6z" fill="var(--sign-navy)"/>
          <path d="M43 26a10 10 0 0 1 9 9M44 19a17 17 0 0 1 15 15" fill="none" stroke="var(--sign-navy)" stroke-width="2.5" stroke-linecap="round"/>
        </svg>
        <p class="phone-pill__number">(555) 617 3489</p>
      </div>
    </section>
  </main>
</body>
</html>
```